Stunning website design for world's unique software

Design only (No coding required)
This website design is linked with a logo design and illustration design contests.

Industry/Entity Type

Software

```html
<!DOCTYPE html>
<html lang="en">
<head>
<meta charset="utf-8">
<title>learnova — learning technology solutions</title>
<link rel="stylesheet" href="https://fonts.googleapis.com/css2?family=Source+Sans+3:wght@300;400;600;700&display=swap">
<style>
:root{
  --blue:#2a8fd6;
  --blue-dark:#1f7cc0;
  --orange:#e8632a;
  --ink:#3d3d3d;
  --muted:#8a8a8a;
  --soft:#ececec;
  --line:#d9d9d9;
  --footer:#333333;
  --footer-deep:#222222;
  --white:#ffffff;
}
*{box-sizing:border-box;margin:0;padding:0}
html,body{width:1200px;height:2379px;overflow:hidden}
body{font-family:"Source Sans 3",Arial,sans-serif;color:var(--ink);background:var(--white);position:relative}
.abs{position:absolute}
a{color:inherit;text-decoration:none}

/* header */
.site-header{position:absolute;left:0;top:0;width:1200px;height:122px;background:var(--white)}
.brand{left:185px;top:40px}
.brand-name{font-size:40px;font-weight:600;color:#4a4a4a;letter-spacing:-0.5px;line-height:1}
.brand-tag{font-size:11px;color:#555;margin-top:2px;letter-spacing:.2px}
.social-top{left:890px;top:12px;display:flex;gap:11px}
.social-top span{width:16px;height:16px;border-radius:3px;background:#6c6c6c;display:block}
.login{left:795px;top:58px;width:88px;height:29px;border-radius:15px;background:var(--blue);color:#fff;font-size:13px;font-weight:700;text-align:center;line-height:29px}
.search{left:890px;top:58px;width:141px;height:29px;border-radius:15px;background:#eaeaea;font-size:11px;color:#999;padding-left:14px;line-height:29px;letter-spacing:.5px}
.search svg{position:absolute;right:12px;top:8px}

.main-nav{position:absolute;left:0;top:124px;width:1200px;height:58px;background:#fff;border-top:1px solid var(--line);border-bottom:1px solid var(--line);box-shadow:0 2px 3px rgba(0,0,0,.06)}
.main-nav ul{list-style:none;position:absolute;left:164px;top:19px;display:flex;gap:28px;font-size:13px;font-weight:600;color:#555;letter-spacing:.6px}

/* hero */
.hero{position:absolute;left:0;top:185px;width:1200px;height:338px;background:linear-gradient(180deg,#2f95dc,#2586cc)}
.hero h1{position:absolute;left:177px;top:48px;width:720px;font-size:48px;line-height:48px;font-weight:700;color:#fff}
.hero p{position:absolute;left:177px;top:153px;width:800px;font-size:14px;line-height:19px;color:#eaf4fb}
.hero .btn-outline{position:absolute;top:230px;height:34px;border:2px solid #fff;border-radius:6px;color:#fff;font-size:17px;font-weight:600;text-align:center;line-height:30px}
.hero .arrow{position:absolute;top:162px}
.hero .dots{position:absolute;left:530px;top:306px;display:flex;gap:12px}
.hero .dots span{width:14px;height:14px;border-radius:50%;border:2px solid #fff}

/* services */
.band-soft{position:absolute;left:0;width:1200px;background:var(--soft)}
.section-title{position:absolute;left:0;width:1200px;text-align:center;font-size:31px;font-weight:600;color:#555}
.service{position:absolute;top:690px;width:190px;text-align:center}
.service svg{display:block;margin:0 auto}
.service h3{font-size:19px;font-weight:600;color:#555;margin-top:6px}
.service p{font-size:12px;line-height:15px;color:#666;margin-top:5px}
.service .more{display:block;font-size:12px;color:var(--orange);margin-top:8px}

/* clients */
.clients{position:absolute;left:0;top:925px;width:1200px;height:114px;background:#fff;border-top:1px solid var(--line);border-bottom:1px solid var(--line)}
.client{position:absolute;top:42px;font-size:22px;color:#222;transform:translateX(-50%);white-space:nowrap}
.client.bold{font-weight:700;color:#1d3f8f;font-size:24px}

/* about */
.about-title{left:164px;top:1096px;font-size:32px;font-weight:600;color:#555}
.about-text{left:164px;top:1140px;width:400px;font-size:18px;line-height:24px;color:var(--muted)}
.btn-solid{position:absolute;height:27px;border-radius:4px;background:var(--blue);color:#fff;font-size:12px;text-align:center;line-height:27px}
.about-photo{left:592px;top:1128px;width:447px;height:241px;border:3px solid #fff;box-shadow:0 0 0 1px #ccc;background:linear-gradient(120deg,#e9eef2 0%,#b9c3cc 40%,#8e949a 70%,#f2f2f2 100%)}

.quote{left:190px;top:1488px;width:820px;text-align:center;font-size:18px;line-height:24px;color:var(--muted)}
.quote-author{left:0;top:1562px;width:1200px;text-align:center;font-size:13px;color:#777;letter-spacing:1px}
.quote-dots{left:586px;top:1598px;display:flex;gap:4px}
.quote-dots span{width:7px;height:7px;border-radius:50%;background:#999}

/* feeds */
.feeds{position:absolute;left:0;top:1639px;width:1200px;height:343px;background:#fff}
.feed-title{position:absolute;top:26px;font-size:17px;color:#444}
.feed-item{position:absolute;width:200px;font-size:12px;line-height:15px;color:#666;padding-left:20px}
.feed-item svg{position:absolute;left:0;top:2px}
.feed-item .meta{display:block;color:#666}
.demo-card{position:absolute;left:740px;top:53px;width:222px;height:251px;background:#fff;box-shadow:0 1px 4px rgba(0,0,0,.18)}
.demo-visual{position:absolute;left:18px;top:8px;width:186px;height:116px;background:linear-gradient(180deg,#f7f7f7,#dcdcdc)}
.demo-card p{position:absolute;left:18px;top:130px;width:190px;font-size:12px;line-height:15px;color:#666}
.shelf-shadow{position:absolute;left:200px;top:1982px;width:800px;height:22px;background:radial-gradient(ellipse at top,rgba(0,0,0,.22),rgba(0,0,0,0) 70%)}

/* footer */
.site-footer{position:absolute;left:0;top:2048px;width:1200px;height:259px;background:var(--footer)}
.footer-title{position:absolute;top:32px;font-size:15px;font-weight:700;color:var(--orange)}
.quick-links{position:absolute;left:169px;top:54px;list-style:none;font-size:12px;line-height:18px;color:#bbb}
.footer-text{position:absolute;font-size:12px;line-height:16px;color:#bbb}
.footer-text b{color:var(--orange);font-weight:600;font-size:14px}
.footer-social{position:absolute;left:661px;top:76px;display:flex;gap:13px}
.footer-social span{width:14px;height:14px;border-radius:50%;background:#d8d8d8;display:block}
.footer-bottom{position:absolute;left:0;top:2307px;width:1200px;height:72px;background:var(--footer-deep)}
.footer-bottom p{position:absolute;left:169px;top:30px;font-size:11px;color:#bbb}
</style>
</head>
<body>

<header class="site-header">
  <div class="abs brand">
    <div class="brand-name">learnova</div>
    <div class="brand-tag">knowledge . talent . performance</div>
  </div>
  <div class="abs social-top" aria-label="Social links">
    <span></span><span></span><span></span><span></span><span></span><span></span>
  </div>
  <a class="abs login" href="#">LOGIN</a>
  <div class="abs search">SEARCH
    <svg width="13" height="13" viewBox="0 0 13 13"><circle cx="5.5" cy="5.5" r="4" fill="none" stroke="#666" stroke-width="1.6"/><line x1="8.5" y1="8.5" x2="12" y2="12" stroke="#666" stroke-width="1.8"/></svg>
  </div>
</header>

<nav class="main-nav">
  <ul>
    <li>HOME</li><li>COMPANY</li><li>PRODUCTS</li><li>SERVICES</li><li>PORFOLIO</li><li>RESOURCES</li><li>BLOG</li>
  </ul>
</nav>

<section class="hero">
  <svg class="arrow" style="left:140px" width="22" height="30" viewBox="0 0 22 30"><path d="M18 3 5 15l13 12" fill="none" stroke="#cfe6f6" stroke-width="5"/></svg>
  <h1>Passionate, Flexible, Curious &amp; Restless</h1>
  <p>Far far away, behind the word mountains, far from the countries Vokalia and Consonantia, there live the blind texts. Separated they live in Bookmarksgrove right at the coast of the Semantics.</p>
  <a class="btn-outline" style="left:188px;width:122px" href="#">Contact us</a>
  <a class="btn-outline" style="left:322px;width:122px" href="#">Services</a>
  <svg class="arrow" style="left:1040px" width="22" height="30" viewBox="0 0 22 30"><path d="M4 3l13 12L4 27" fill="none" stroke="#cfe6f6" stroke-width="5"/></svg>
  <div class="dots"><span></span><span></span><span></span><span></span></div>
</section>

<div class="band-soft" style="top:523px;height:402px"></div>
<h2 class="section-title" style="top:578px">A leading provider of learning technology solutions</h2>

<div class="service" style="left:183px">
  <svg width="48" height="48" viewBox="0 0 48 48" fill="none" stroke="#e8632a" stroke-width="2.5"><circle cx="24" cy="22" r="17"/><path d="M14 40l10-18 10 18"/><circle cx="24" cy="22" r="3"/></svg>
  <h3>Lorem Ipsum</h3>
  <p>Lorem Ipsum is simply dummy text of the printing and typesetting industry. Lorem Ipsum has been the</p>
  <span class="more">more</span>
</div>
<div class="service" style="left:381px">
  <svg width="52" height="48" viewBox="0 0 52 48" fill="none" stroke="#e8632a" stroke-width="2.5"><rect x="3" y="6" width="46" height="30" rx="2"/><path d="M20 44h12M26 36v8M16 28l14-14"/></svg>
  <h3>Lorem Ipsum is simply</h3>
  <p>Lorem Ipsum is simply dummy text of the printing and typesetting industry. Lorem Ipsum has been the</p>
  <span class="more">more</span>
</div>
<div class="service" style="left:608px">
  <svg width="52" height="48" viewBox="0 0 52 48" fill="none" stroke="#e8632a" stroke-width="3"><path d="M16 12 4 24l12 12M36 12l12 12-12 12M30 8 22 40"/></svg>
  <h3>Lorem Ipsum</h3>
  <p>Lorem Ipsum is simply dummy text of the printing and typesetting industry. Lorem Ipsum has been the</p>
  <span class="more">more</span>
</div>
<div class="service" style="left:827px">
  <svg width="60" height="48" viewBox="0 0 60 48" fill="none" stroke="#e8632a" stroke-width="2.5"><rect x="8" y="4" width="40" height="28" rx="2"/><path d="M20 40h16M28 32v8"/><rect x="2" y="20" width="12" height="22" rx="2"/><rect x="44" y="22" width="14" height="20" rx="2"/></svg>
  <h3>Lorem Ipsum is simply</h3>
  <p>Lorem Ipsum is simply dummy text of the printing and typesetting industry. Lorem Ipsum has been the</p>
  <span class="more">more</span>
</div>

<section class="clients" aria-label="Clients">
  <svg class="abs" style="left:138px;top:40px" width="20" height="30" viewBox="0 0 20 30"><path d="M16 3 4 15l12 12" fill="none" stroke="#bbb" stroke-width="5"/></svg>
  <span class="client" style="left:225px">VELMONT</span>
  <span class="client bold" style="left:383px">ORBIQ</span>
  <span class="client" style="left:547px;color:#c2185b">Harvest &amp; Co</span>
  <span class="client" style="left:722px;font-weight:700">NORDVALE</span>
  <span class="client" style="left:840px">VELMONT</span>
  <span class="client bold" style="left:972px">ORBIQ</span>
  <svg class="abs" style="left:1040px;top:40px" width="20" height="30" viewBox="0 0 20 30"><path d="M4 3l12 12L4 27" fill="none" stroke="#bbb" stroke-width="5"/></svg>
</section>

<div class="band-soft" style="top:1040px;height:599px"></div>
<h2 class="abs about-title">About Us</h2>
<p class="abs about-text">Lorem Ipsum decided to leave for the far World of Grammar. The Big Oxmox advised her not to do so, because there were thousands of bad Commas, wild Question Marks and devious Semikoli</p>
<a class="btn-solid" style="left:172px;top:1277px;width:90px" href="#">Read more</a>
<div class="abs about-photo" role="img" aria-label="Photo of a team of three colleagues working together at a laptop"></div>

<h2 class="section-title" style="top:1418px">What the clients say</h2>
<p class="abs quote">Lorem Ipsum decided to leave for the far World of Grammar. The Big Oxmox advised her not to do so, because there were thousands of bad Commas, wild Question Marks and devious Semikoli</p>
<div class="abs quote-author">– ALEX MORROW –</div>
<div class="abs quote-dots"><span></span><span></span><span></span></div>

<section class="feeds">
  <h3 class="feed-title" style="left:256px">Latest News</h3>
  <div class="feed-item" style="left:256px;top:63px"><svg width="13" height="13" viewBox="0 0 13 13"><rect x="1" y="2" width="11" height="10" fill="none" stroke="#777" stroke-width="1.3"/><line x1="1" y1="5" x2="12" y2="5" stroke="#777"/></svg>Lorem Ipsum is simply dummy text of the printing and typesetting industry. Lorem Ipsum has been the <span class="meta">September 2014</span></div>
  <div class="feed-item" style="left:256px;top:136px"><svg width="13" height="13" viewBox="0 0 13 13"><rect x="1" y="2" width="11" height="10" fill="none" stroke="#777" stroke-width="1.3"/><line x1="1" y1="5" x2="12" y2="5" stroke="#777"/></svg>Lorem Ipsum is simply dummy text of the printing and typesetting industry. Lorem Ipsum has been the <span class="meta">September 2014</span></div>
  <div class="feed-item" style="left:256px;top:208px"><svg width="13" height="13" viewBox="0 0 13 13"><rect x="1" y="2" width="11" height="10" fill="none" stroke="#777" stroke-width="1.3"/><line x1="1" y1="5" x2="12" y2="5" stroke="#777"/></svg>Lorem Ipsum is simply dummy text of the printing and typesetting industry. Lorem Ipsum has been the <span class="meta">September 2014</span></div>
  <a class="btn-solid" style="left:280px;top:274px;width:72px;height:22px;line-height:22px" href="#">View all</a>

  <h3 class="feed-title" style="left:497px">From Our Blog</h3>
  <div class="feed-item" style="left:497px;top:63px"><svg width="13" height="13" viewBox="0 0 13 13"><circle cx="6.5" cy="6.5" r="5" fill="none" stroke="#777" stroke-width="1.3"/><path d="M6.5 3.5v3h2.5" fill="none" stroke="#777"/></svg>Lorem Ipsum is simply dummy text of the printing and typesetting industry. Lorem Ipsum has been the industry's <span class="meta">- mara lind -</span></div>
  <div class="feed-item" style="left:497px;top:134px"><svg width="13" height="13" viewBox="0 0 13 13"><circle cx="6.5" cy="6.5" r="5" fill="none" stroke="#777" stroke-width="1.3"/><path d="M6.5 3.5v3h2.5" fill="none" stroke="#777"/></svg>Lorem Ipsum is simply dummy text of the printing and typesetting industry. Lorem Ipsum has been the industry's <span class="meta">- mara lind -</span></div>
  <div class="feed-item" style="left:497px;top:205px"><svg width="13" height="13" viewBox="0 0 13 13"><circle cx="6.5" cy="6.5" r="5" fill="none" stroke="#777" stroke-width="1.3"/><path d="M6.5 3.5v3h2.5" fill="none" stroke="#777"/></svg>Lorem Ipsum is simply dummy text of the printing and typesetting industry. Lorem Ipsum has been the industry's <span class="meta">- mara lind -</span></div>
  <a class="btn-solid" style="left:518px;top:274px;width:74px;height:22px;line-height:22px" href="#">Visit Blog</a>

  <h3 class="feed-title" style="left:737px">Product Demo</h3>
  <div class="demo-card">
    <div class="demo-visual" role="img" aria-label="Illustration of the product shown on a monitor, laptop, tablet and phone"></div>
    <p>Lorem Ipsum is simply dummy text of the printing and typesetting industry. Lorem</p>
  </div>
</section>
<div class="shelf-shadow"></div>

<footer class="site-footer">
  <h4 class="footer-title" style="left:169px">Quick Links</h4>
  <ul class="quick-links">
    <li>Home</li><li>Company</li><li>Products</li><li>Services</li><li>Portfolio</li><li>Careers</li><li>Resources</li><li>Blog</li>
  </ul>
  <h4 class="footer-title" style="left:367px">Get in Touch</h4>
  <p class="footer-text" style="left:367px;top:74px;width:210px">Lorem Ipsum is simply dummy text of the printing and typesetting industry. Lorem</p>
  <p class="footer-text" style="left:367px;top:120px"><b>Tel. :</b> +10 55 0123 4567</p>
  <p class="footer-text" style="left:367px;top:140px"><b>Email :</b> hello@learnova.example</p>
  <h4 class="footer-title" style="left:661px">Stay Connected</h4>
  <div class="footer-social" aria-label="Social links">
    <span></span><span></span><span></span><span></span><span></span><span></span><span></span><span></span>
  </div>
</footer>
<div class="footer-bottom"><p>Copyright © 2014</p></div>

</body>
</html>
```